Join Hour 4 Fun business card

Join Hour 4 Fun is a national UK campaign that promotes the value of play for children. The website has recently undergone a redesign and will soon be going live, this business card design will need to reflect the new website's design and colour scheme, etc.
Key wording/info for inclusion (front)
- Strapline titles
A small Romp each morning (in caps)
giving you great free play ideas, everyday!
- Logo
Key wording for inclusion (rear)
- Download our free play app - Join Hour 4 Fun
- Visit our website - www.joinhour4fun.co.uk
- To share hints and tips with other parents
www.facebook.com/joinhourforfun
- Want to get involved in the campaign? No matter who you are we would love to hear from you! Email - getinvolved@joinhourforfun.co.uk
Social media icons
Facebook facebook.com/joinhour4fun
Twitter @joinhour4fun
Youtube youtube.com/joinhourforfun
The target audience is parents of young children up to the age of 12.
Please note that all attached graphics are the property of the Northern Craft & Pastime Guild and must only be used for the purpose of this project.
Updates
Please note the design we are seeking will be in a business card 'shape' but will not be for a specific 'person' or name as such. We are looking for a colourful and modern design which is not 'corporate. Thank you.
Target Market(s)
Industry/Entity Type
Business
Look and feel

```html
<!DOCTYPE html>
<html lang="en">
<head>
<meta charset="utf-8">
<title>Join Hour 4 Fun – Business Card</title>
<link rel="stylesheet" href="https://fonts.googleapis.com/css2?family=Comic+Neue:wght@400;700&family=Open+Sans:ital,wght@1,400&display=swap">
<style>
  :root {
    --sky-blue: #1ab0e6;
    --meadow-green: #8cc63f;
    --meadow-light: #bcdc5a;
    --paper: #ffffff;
    --ink: #1a1a1a;
    --fun-pink: #e8587a;
    --play-purple: #5b3f8f;
    --sun-yellow: #f5d400;
    --brand-purple: #6a4c9c;
  }
  html, body {
    margin: 0;
    padding: 0;
    width: 1200px;
    height: 741px;
    overflow: hidden;
    background: var(--paper);
  }
  .card {
    position: relative;
    width: 1200px;
    height: 741px;
    overflow: hidden;
    background: var(--paper);
    font-family: "Comic Neue", "Comic Sans MS", cursive;
  }
  .card__backdrop {
    position: absolute;
    inset: 0;
    width: 1200px;
    height: 741px;
  }
  .photo-area {
    position: absolute;
    left: 520px;
    top: 225px;
    width: 620px;
    height: 480px;
    border-radius: 50%;
    background: radial-gradient(ellipse at 55% 50%,
      rgba(226, 196, 176, 0.85) 0%,
      rgba(236, 214, 196, 0.7) 35%,
      rgba(245, 232, 222, 0.4) 60%,
      rgba(255, 255, 255, 0) 75%);
  }
  .tree-area {
    position: absolute;
    left: 0;
    top: 485px;
    width: 140px;
    height: 190px;
    border-radius: 50% 50% 40% 40%;
    background: radial-gradient(ellipse at 50% 40%,
      rgba(110, 160, 60, 0.9) 0%,
      rgba(140, 190, 80, 0.6) 55%,
      rgba(255, 255, 255, 0) 75%);
  }
  .brand {
    position: absolute;
    left: 44px;
    top: 135px;
    width: 272px;
    height: 272px;
    border-radius: 50%;
    background: var(--paper);
    display: flex;
    align-items: center;
    justify-content: center;
    text-align: center;
  }
  .brand__name {
    font-weight: 700;
    font-size: 40px;
    line-height: 1.05;
    color: var(--brand-purple);
  }
  .strapline {
    position: absolute;
    right: 24px;
    top: 72px;
    margin: 0;
    font-weight: 700;
    font-size: 44px;
    letter-spacing: 1px;
    color: var(--paper);
    text-shadow: 3px 3px 0 var(--ink);
    white-space: nowrap;
  }
  .tagline {
    position: absolute;
    right: 24px;
    top: 160px;
    margin: 0;
    font-family: "Open Sans", Arial, sans-serif;
    font-style: italic;
    font-size: 25px;
    color: var(--ink);
    white-space: nowrap;
  }
  .slogan {
    position: absolute;
    margin: 0;
    font-weight: 400;
    white-space: nowrap;
    line-height: 1;
  }
  .slogan--fun { left: 384px; top: 368px; font-size: 96px; color: var(--fun-pink); }
  .slogan--play { left: 257px; top: 482px; font-size: 60px; color: var(--play-purple); }
  .slogan--involved { left: 586px; top: 518px; font-size: 84px; color: var(--sun-yellow); }
</style>
</head>
<body>
  <main class="card">
    <svg class="card__backdrop" viewBox="0 0 1200 741" aria-hidden="true">
      <defs>
        <linearGradient id="meadow" x1="0" y1="0" x2="0" y2="1">
          <stop offset="0" stop-color="var(--meadow-light)"/>
          <stop offset="1" stop-color="var(--meadow-green)"/>
        </linearGradient>
      </defs>
      <path class="sky-band" fill="var(--sky-blue)"
        d="M0 0 H1200 V240 C1130 215 1070 230 1000 232 C930 234 880 205 810 205 C740 205 700 222 640 220 C560 218 520 190 450 190 C380 190 330 172 260 165 C180 158 90 160 0 150 Z"/>
      <path class="meadow-band" fill="url(#meadow)"
        d="M0 620 C60 640 120 655 200 670 C300 690 380 680 470 672 C560 664 620 690 720 690 C820 690 880 668 980 672 C1060 676 1130 690 1200 690 V741 H0 Z"/>
    </svg>

    <div class="photo-area" role="img" aria-label="Photo of smiling children lying in a circle, heads together, making binocular shapes with their hands, faded softly into the background"></div>
    <div class="tree-area" role="img" aria-label="Illustration of a small green apple tree on the hill"></div>

    <div class="brand">
      <span class="brand__name">Join Hour<br>4 Fun</span>
    </div>

    <h1 class="strapline">A SMALL ROMP EACH MORNING</h1>
    <p class="tagline">... giving you great free play ideas, everyday!</p>

    <p class="slogan slogan--fun">fun forever</p>
    <p class="slogan slogan--play">play right now</p>
    <p class="slogan slogan--involved">get involved</p>
  </main>
</body>
</html>
```